Marketing , Sales and Distribution Website

This website/this business is specifically to start an international marketing, sales and distribution business - no more than 5 pages - one page design with supporting pages, a strong "call to action" design - lead generation design - Modern - can be easily upgraded.

Target Market(s)

Industrial, engineering, Art, technology, food products, fashion and accessories

Industry/Entity Type

Marketing

Coding

Coded - Design and coding required

Font styles to use
Sans Serif

Requirements
Must have
• user friendly. Fast upload time - space for content. Most have strategic "call to action" lead generation opportunities - space for video, links to social media. room for articles, blogs and upcoming tradeshows - modern interactive website - easy to upgrade in the future. Lastly a link or Tab to a one page site dedicated to mobile marketing subscriptions
Nice to have
• Client login area - backend CRM integration - Hubspot
• I am open to suggestions to make this site attractive for companies who import/export goods - or generate leads of companies who wish to import/export their products to the USA - a lot of this information is in the attachment.

```html
<!DOCTYPE html>
<html lang="en">
<head>
<meta charset="utf-8">
<title>Brightvale Marketing</title>
<link rel="stylesheet" href="https://fonts.googleapis.com/css2?family=Fira+Sans+Condensed:wght@400;500;600;700&family=Fira+Sans:wght@300;400;600&family=Open+Sans:wght@400;600&display=swap">
<style>
:root{
  --blue:#2f4fa6;
  --blue-deep:#243f8c;
  --blue-light:#4a6fd0;
  --red:#ef3a4c;
  --red-deep:#e22a3e;
  --ink:#222428;
  --grey:#8a8d93;
  --pale:#9fb5e2;
  --highlight:#9cb8ff;
  --white:#ffffff;
  --field:#f3f5fa;
}
*{margin:0;padding:0;box-sizing:border-box}
html,body{width:1200px;height:3346px;overflow:hidden;background:var(--white)}
body{position:relative;font-family:"Open Sans",sans-serif;color:var(--ink)}
.abs{position:absolute}
.cond{font-family:"Fira Sans Condensed",sans-serif}
.center{left:0;width:1200px;text-align:center}
.white{color:var(--white)}

/* hero */
.hero{left:0;top:0;width:1200px;height:600px;background:linear-gradient(120deg,#3556b3 0%,#2c4aa3 45%,#4168cc 75%,#2a469c 100%)}
.brand{left:0;top:0;width:128px;height:128px;background:var(--blue-light);display:flex;align-items:center;justify-content:center;color:var(--white);font-family:"Fira Sans Condensed",sans-serif;font-weight:600;font-size:20px}
.nav-link{top:53px;color:var(--white);font-family:"Fira Sans Condensed",sans-serif;font-weight:600;font-size:14px}
.nav-link.active{color:#b9c8f0}
.phone{left:950px;top:52px;color:var(--white);font-family:"Fira Sans Condensed",sans-serif;font-weight:600;font-size:14px;display:flex;align-items:center;gap:12px}
.login{left:1152px;top:46px;width:26px;height:26px;background:#6f8fdc}
.hero-title{left:261px;top:268px;color:var(--white);font-family:"Fira Sans Condensed",sans-serif;font-weight:600;font-size:31px;line-height:35px}
.btn-outline{display:flex;align-items:center;justify-content:center;border:2px solid var(--white);border-radius:26px;color:var(--white);font-family:"Fira Sans Condensed",sans-serif;font-weight:600;font-size:14px}
.dot{width:24px;height:24px;border:1.5px solid rgba(255,255,255,.8);border-radius:50%}
.side-dot{left:1070px}

/* intro */
.intro{left:0;top:600px;width:1200px;height:415px;background:linear-gradient(135deg,#f2485a 0%,var(--red) 50%,var(--red-deep) 100%)}
.video{left:600px;top:600px;width:453px;height:415px;background:linear-gradient(135deg,#e9eef3 0%,#b8c2cf 45%,#3c4658 100%)}
.play{left:794px;top:769px;width:76px;height:76px;border-radius:50%;background:rgba(255,255,255,.85)}

/* services */
.sec-title{font-family:"Fira Sans Condensed",sans-serif;font-size:27px;font-weight:600;color:var(--ink)}
.sec-sub{font-size:13px;color:var(--grey)}
.svc-icon{width:130px;height:130px;border-radius:50%;top:1179px;border:1.5px solid #b8c6e6}
.svc{top:1336px;width:320px;text-align:center}
.svc h3{font-family:"Fira Sans Condensed",sans-serif;font-size:17px;font-weight:600}
.svc p{font-size:13px;color:var(--grey);line-height:20px;margin-top:8px}

/* subscribe */
.subscribe{left:0;top:1483px;width:1200px;height:392px;background:linear-gradient(120deg,#3b3536 0%,#2e2a2c 50%,#463c3a 100%)}
.sub-title{top:1543px;font-family:"Fira Sans",sans-serif;font-weight:300;font-size:33px;line-height:41px;color:var(--white)}
.sub-title b{font-family:"Fira Sans Condensed",sans-serif;color:var(--highlight);font-weight:500}
.email{left:500px;top:1677px;width:200px;border-bottom:1px solid rgba(255,255,255,.45);padding-bottom:12px;color:rgba(255,255,255,.75);font-size:14px;text-align:center}
.btn-red{left:462px;top:1755px;width:276px;height:47px;border-radius:26px;background:var(--red);color:var(--white);display:flex;align-items:center;justify-content:center;font-family:"Fira Sans Condensed",sans-serif;font-weight:600;font-size:14px}

/* blog */
.post{top:2034px;width:283px}
.thumb{width:283px;height:187px}
.thumb.desk{background:linear-gradient(135deg,#f4f4f4 0%,#d9d9d9 55%,#2c2c2c 100%)}
.thumb.leaf{background:radial-gradient(circle at 50% 55%,#3d8fd3 0%,#58a73a 35%,#8dc73f 70%,#c6e07a 100%)}
.date{font-size:11px;color:var(--red);margin-top:27px}
.post h3{font-family:"Fira Sans Condensed",sans-serif;font-weight:600;font-size:16px;line-height:24px;margin-top:9px;color:var(--ink)}
.post h3.ul span{border-bottom:1px solid var(--ink)}
.post p{font-size:12.5px;color:#5b5e63;line-height:20px;margin-top:12px}
.read{margin-top:27px;width:121px;height:37px;border:2px solid #cfdaf0;border-radius:20px;display:flex;align-items:center;justify-content:center;font-family:"Fira Sans Condensed",sans-serif;font-size:13px;font-weight:600;color:var(--pale)}
.read.filled{background:var(--pale);border-color:var(--pale);color:var(--white)}

/* footer */
.contact{left:0;top:2545px;width:1200px;height:477px;background:linear-gradient(135deg,#2f4ea5 0%,var(--blue-deep) 100%)}
.contact-panel{left:600px;top:2545px;width:600px;height:477px;background:linear-gradient(135deg,#3d5fbd 0%,#2d4b9f 60%,#3356b3 100%)}
.foot-h{font-family:"Fira Sans Condensed",sans-serif;font-size:17px;font-weight:600;color:var(--white)}
.small{font-size:13.5px;line-height:21px;color:var(--white)}
.social-row{left:147px;top:2814px;display:flex;gap:14px}
.social-row .dot{width:30px;height:30px}
.field{left:656px;width:341px;height:36px;background:var(--field);padding:0 16px;font-size:12px;color:#6d7280;display:flex;align-items:center}
.send{left:673px;top:2914px;width:38px;height:38px;border-radius:50%;background:var(--red)}
.map{left:0;top:3022px;width:1200px;height:324px;background:linear-gradient(180deg,#e4e5e7 0%,#d8d9db 100%)}
</style>
</head>
<body>

<!-- hero -->
<div class="abs hero" role="img" aria-label="Photo of blue glass office towers seen from below"></div>
<div class="abs brand">Brightvale</div>
<span class="abs nav-link" style="left:183px">Brightvale</span>
<span class="abs nav-link active" style="left:259px">Distribution</span>
<span class="abs nav-link" style="left:375px">Marketing</span>
<span class="abs nav-link" style="left:477px">Sales</span>
<span class="abs nav-link" style="left:546px">News</span>
<span class="abs nav-link" style="left:618px">Contact Us</span>
<div class="abs phone">
  <svg width="14" height="14" viewBox="0 0 24 24" fill="#cfd9f5"><path d="M6.6 10.8a15 15 0 0 0 6.6 6.6l2.2-2.2c.3-.3.7-.4 1-.2 1.1.4 2.3.6 3.6.6.6 0 1 .4 1 1V20c0 .6-.4 1-1 1A17 17 0 0 1 3 4c0-.6.4-1 1-1h3.5c.6 0 1 .4 1 1 0 1.3.2 2.5.6 3.6.1.3 0 .7-.2 1z"/></svg>
  +1 555-014-2270
</div>
<div class="abs login"></div>
<h1 class="abs hero-title">Do you have<br>product or Service Idea to Market?<br>No Need to get Confussed!</h1>
<div class="abs btn-outline" style="left:261px;top:406px;width:165px;height:47px">I'm Here to Help</div>
<div class="abs dot side-dot" style="top:238px"></div>
<div class="abs dot side-dot" style="top:279px;background:rgba(255,255,255,.5)"></div>
<div class="abs dot side-dot" style="top:321px"></div>
<div class="abs dot side-dot" style="top:364px"></div>
<div class="abs dot side-dot" style="top:406px"></div>

<!-- intro -->
<div class="abs intro"></div>
<div class="abs" style="left:89px;top:673px;width:174px;height:1px;background:rgba(255,255,255,.7)"></div>
<h2 class="abs cond white" style="left:147px;top:706px;font-size:29px;font-weight:600">Brightvale Marketing</h2>
<p class="abs white" style="left:147px;top:750px;width:400px;font-size:14px;line-height:22px">If your plans include developing sales collateral, launching a new product, or redesigning a web site, you will want to know how Brightvale can help you Utilizing creative flair and award winning agency.</p>
<div class="abs btn-outline" style="left:147px;top:903px;width:174px;height:38px;font-size:13px">Get Free Consulting</div>
<div class="abs video" role="img" aria-label="Video still of two businessmen reviewing documents"></div>
<div class="abs play"></div>
<svg class="abs" style="left:820px;top:791px" width="28" height="32" viewBox="0 0 28 32"><path d="M2 2 L26 16 L2 30 Z" fill="#5a6275"/></svg>

<!-- services -->
<h2 class="abs center sec-title" style="top:1083px">What We Do</h2>
<p class="abs center sec-sub" style="top:1121px">Service we provided in those categories</p>
<div class="abs svc-icon" style="left:223px" role="img" aria-label="Distribution icon with arrows spreading outward"></div>
<div class="abs svc-icon" style="left:533px;background:#b8c9ee;border-color:#b8c9ee" role="img" aria-label="Marketing icon of a chart on a screen"></div>
<div class="abs svc-icon" style="left:845px" role="img" aria-label="Sales icon of a price tag"></div>
<div class="abs svc" style="left:128px"><h3>Distribution</h3><p>Establish distribution in United States<br>simply dummy text</p></div>
<div class="abs svc" style="left:438px"><h3><span style="border-bottom:1px solid var(--ink)">Marketing</span></h3><p>On/Off shelf marketing, creating a<br>demand dummy text</p></div>
<div class="abs svc" style="left:750px"><h3>Sales</h3><p>Trade shows assistance and promotions<br>simply dummy text</p></div>

<!-- subscribe -->
<div class="abs subscribe" role="img" aria-label="Dim photo of a team meeting around a table"></div>
<h2 class="abs center sub-title">We are <b>Spontaneous, Professional</b> but <b>Fun</b>, and <b>Encouraging</b><br>team to get Success for you !</h2>
<div class="abs email">Enter your email ...</div>
<div class="abs btn-red">To know how Subscribe here !</div>

<!-- blog -->
<h2 class="abs center sec-title" style="top:1944px">Latest Updates</h2>
<p class="abs center sec-sub" style="top:1983px">The official blog of Brightvale Marketing</p>
<article class="abs post" style="left:147px">
  <div class="thumb desk" role="img" aria-label="Photo of a card beside a laptop keyboard"></div>
  <div class="date">18.05.2016 | BY ADMIN</div>
  <h3 class="ul"><span>Complete Guide to the E-Commerce &amp;</span><br><span>Internet Business</span></h3>
  <p>Working in a business field that's as com-petitive as our is (legal help), we needed some extra piece of analytics ...</p>
  <div class="read">Read More</div>
</article>
<article class="abs post" style="left:457px">
  <div class="thumb leaf" role="img" aria-label="Photo of a hand holding a globe on a green leaf"></div>
  <div class="date">18.05.2016 | BY ADMIN</div>
  <h3>Complete Guide to the Technology<br>(CleanTech) Industry</h3>
  <p>Working in a business field that's as com-petitive as our is (legal help), we needed some extra piece of analytics ...</p>
  <div class="read filled">Read More</div>
</article>
<article class="abs post" style="left:769px">
  <div class="thumb desk" role="img" aria-label="Photo of a card beside a laptop keyboard"></div>
  <div class="date">18.05.2016 | BY ADMIN</div>
  <h3 class="ul"><span>Complete Guide to the E-Commerce &amp;</span><br><span>Internet Business</span></h3>
  <p>Working in a business field that's as com-petitive as our is (legal help), we needed some extra piece of analytics ...</p>
  <div class="read">Read More</div>
</article>

<!-- contact -->
<div class="abs contact"></div>
<div class="abs contact-panel" role="img" aria-label="Faint photo of blue office towers"></div>
<h4 class="abs foot-h" style="left:147px;top:2615px">Contact Us</h4>
<div class="abs white" style="left:147px;top:2653px;font-size:21px">Call: +1 555-014-2270</div>
<div class="abs small" style="left:147px;top:2683px">hello@brightvalemarketing.com</div>
<div class="abs small" style="left:147px;top:2722px">812 Harbor Lane Portside,<br>WA 98000</div>
<div class="abs small" style="left:147px;top:2782px">Get Social:</div>
<div class="abs social-row"><div class="dot"></div><div class="dot"></div><div class="dot"></div><div class="dot"></div><div class="dot"></div></div>
<div class="abs small" style="left:147px;top:2910px">© 2017 Brightvale Marketing.<br>All rights reserved.</div>
<h4 class="abs foot-h" style="left:656px;top:2615px">Need Help ? Send Us Message</h4>
<div class="abs field" style="top:2658px">Name</div>
<div class="abs field" style="top:2707px">Email</div>
<div class="abs field" style="top:2756px">Phone</div>
<div class="abs field" style="top:2806px;height:128px;align-items:flex-start;padding-top:10px">Message</div>
<div class="abs send"></div>
<svg class="abs" style="left:683px;top:2924px" width="18" height="18" viewBox="0 0 24 24"><path d="M2 12 L22 3 L15 22 L12 13 Z" fill="#fff"/></svg>

<!-- map -->
<div class="abs map" role="img" aria-label="Grey street map of the office area"></div>

</body>
</html>
```